Creating a Label for a new CBD Vape Line call "Brizel".

This will be a project that will create the first label design on a BRIZEL Vape product that is being rolled out in Colorado. The vape line will cater to high concentration CBD Vape sold in disposable vape pens and replacement cartridge's. In the sea of vape pens we want our packaging to stand out with a bold, bright, clean, abstract design that will highlight the brand "BRIZEL" in a font that stands out and is quickly recognized. The target demographic for this line is 18-29 years of age. The mock up of the brizel vape picture does not meet our marketing desire, I just wanted to show you the approximate shape and size of the label and that the font used for the label will be added to the actual pen. This pen will have 100% CBD, cut with all natural terpenes with no need for chemicals like PG or VG, not many on the market like that. I included several marketing logos that caught our eye with other type product, please look at those as examples but we are open to creativity.

Target Market(s)

18-29 year old

Industry/Entity Type

CBD and Vape

Font styles to use
Serif
Sans Serif

Requirements
Must have
• bold, colorful, fun, eye catching
Nice to have
• Several brand ideas presented to give the flavor of the marketing. The example font on the prototype is not 'cool enough' to use, we'd like that name BRIZEL to look and feel brizzzel. :-)
Should not have
• old school, boring, dull colors, small font

```html
<!DOCTYPE html>
<html lang="en">
<head>
<meta charset="utf-8">
<title>Brizel Nova Vape Label</title>
<link href="https://fonts.googleapis.com/css2?family=Open+Sans:wght@600;700&family=Source+Code+Pro:wght@400;600&display=swap" rel="stylesheet">
<style>
  :root {
    --mint: #a9e8bb;
    --foil: #a9b0b0;
    --foil-light: #c3c9c9;
    --purple: #5b2bb0;
    --deep-purple: #4a1f8f;
    --ink: #1c1c2a;
    --white: #f4f6ff;
    --badge-red: #c8202c;
  }
  * { margin: 0; padding: 0; box-sizing: border-box; }
  html, body { width: 847px; height: 1200px; overflow: hidden; }
  body { background: var(--mint); position: relative; font-family: "Open Sans", sans-serif; }

  .pouch {
    position: absolute; left: 215px; top: 76px; width: 448px; height: 665px;
    background: linear-gradient(180deg, var(--foil-light) 0%, var(--foil) 12%, var(--foil) 100%);
    border-radius: 3px;
  }
  .pouch-seal { position: absolute; left: 0; right: 0; top: 50px; height: 1px; background: #8e9595; }
  .pouch-hang-hole {
    position: absolute; left: 198px; top: 16px; width: 69px; height: 14px;
    border-radius: 7px; background: var(--mint);
  }

  .label {
    position: absolute; width: 365px; height: 182px; overflow: hidden;
    background:
      radial-gradient(ellipse 60% 55% at 85% 25%, rgba(248,240,170,.95), transparent 70%),
      radial-gradient(ellipse 50% 50% at 30% 10%, rgba(200,225,250,.9), transparent 70%),
      radial-gradient(ellipse 90% 30% at 50% 80%, rgba(90,200,190,.85), transparent 70%),
      linear-gradient(180deg, #a9a8e6 0%, #cfe6ee 35%, #e6efc8 55%, #6cc3c0 78%, #3e57d8 100%);
  }
  .label-on-pouch { left: 247px; top: 204px; transform: scale(1.04); transform-origin: 0 0; }
  .label-flat { left: 252px; top: 792px; }

  .age-badge {
    position: absolute; left: 13px; top: 13px; width: 26px; height: 26px;
    border: 2px solid var(--badge-red); border-radius: 50%;
    font-weight: 700; font-size: 11px; color: var(--purple);
    display: flex; align-items: center; justify-content: center;
  }
  .label-on-pouch .age-badge { border-color: var(--purple); }
  .age-badge sup { font-size: 7px; color: var(--badge-red); }

  .brand-name {
    position: absolute; left: 62px; top: 10px; width: 266px;
    font-weight: 700; font-size: 76px; line-height: 1; color: var(--purple);
    letter-spacing: 4px; white-space: nowrap;
  }
  .product-name {
    position: absolute; left: 70px; top: 103px;
    font-weight: 700; font-size: 18px; line-height: 24px; color: var(--ink);
  }
  .strength {
    position: absolute; left: 196px; top: 107px; width: 130px; height: 19px;
    background: var(--deep-purple); color: var(--white);
    font-family: "Source Code Pro", monospace; font-weight: 600; font-size: 15px;
    display: flex; align-items: center; justify-content: center; word-spacing: 4px;
  }
  .rule { position: absolute; background: rgba(40,40,90,.55); }
  .rule-top { left: 64px; top: 127px; width: 262px; height: 1px; }
  .rule-bottom { left: 64px; top: 164px; width: 262px; height: 1px; }
  .rule-divider { left: 179px; top: 127px; width: 1px; height: 40px; }

  .website {
    position: absolute; left: 69px; top: 137px;
    font-family: "Source Code Pro", monospace; font-size: 12px; color: var(--white);
  }
  .disclaimer {
    position: absolute; left: 184px; top: 133px; width: 142px;
    font-family: "Source Code Pro", monospace; font-size: 5.4px; line-height: 6.2px;
    color: var(--white); text-align: center; white-space: nowrap;
  }

  .brand-display {
    position: absolute; left: 239px; top: 1020px; width: 372px;
    font-weight: 700; font-size: 124px; line-height: 1; color: var(--purple);
    letter-spacing: 4px; white-space: nowrap;
  }
</style>
</head>
<body>
  <div class="pouch">
    <div class="pouch-hang-hole"></div>
    <div class="pouch-seal"></div>
  </div>

  <div class="label label-on-pouch">
    <div class="age-badge">21<sup>+</sup></div>
    <div class="brand-name">Brizel</div>
    <div class="product-name">Nova VAPE</div>
    <div class="strength">450mg CBD</div>
    <div class="rule rule-top"></div>
    <div class="rule rule-divider"></div>
    <div class="rule rule-bottom"></div>
    <div class="website">BrizelCBD.com</div>
    <p class="disclaimer">These statements have not been evaluated<br>by the Food and Drug Administration.<br>This product is not intented to trat<br>cure or prevent any disease.</p>
  </div>

  <div class="label label-flat">
    <div class="age-badge">21<sup>+</sup></div>
    <div class="brand-name">Brizel</div>
    <div class="product-name">Nova VAPE</div>
    <div class="strength">450mg CBD</div>
    <div class="rule rule-top"></div>
    <div class="rule rule-divider"></div>
    <div class="rule rule-bottom"></div>
    <div class="website">BrizelCBD.com</div>
    <p class="disclaimer">These statements have not been evaluated<br>by the Food and Drug Administration.<br>This product is not intented to trat<br>cure or prevent any disease.</p>
  </div>

  <div class="brand-display">Brizel</div>
</body>
</html>
```